artist "stamp" design

Im a young artist. I`m making a stamp with my information so i can make homemade business cards, so I need the following information to look good together and simple to read:

Lucila Marbán Oteiza

www.lumaroti.com

lucilamo47@vextramail.com

i want a very clan look, but with some personality. a simple logo or "look" would be great but nothing to fancy.

An idea I had was to make it look like it was written with a typewriter or a concept like that...be creative! thank you!
Updates

I don't want any image or icon, just letters, I need it to be compacto, I'm making a stamp

I don't want it to say photography 

I dont want my name to take over so it should stay close to the size as the rest of the info.

all my info should be included, this is not a logo its a design for a stamp meant to fin in a business card.

Target Market(s)

I'm a photographer, I want something very simple and I need this to make a stamp that ill use to pit on my cards and CV. I want something simple and modern

Industry/Entity Type

Business

Logo Text

Lucila Marbán Oteiza

Logo styles of interest
Abstract Logo
Wordmark Logo
Lettermark Logo
Font styles to use
Serif
Sans Serif

Requirements
Must have
• Has to look young and fresh
Nice to have
• Have to see how it looks on a business card with website and and email
Should not have
• Images

```html
<!DOCTYPE html>
<html lang="es">
<head>
<meta charset="utf-8">
<title>Lucila Marbán Oteiza — Sello de contacto</title>
<link rel="stylesheet" href="https://fonts.googleapis.com/css2?family=Poppins:wght@500;600&display=swap">
<style>
  :root {
    --paper: #ffffff;
    --ink: #231f20;
  }
  html, body {
    margin: 0;
    padding: 0;
    width: 1200px;
    height: 1000px;
    overflow: hidden;
    background: var(--paper);
  }
  .stamp-canvas {
    display: block;
    width: 1200px;
    height: 1000px;
  }
  .stamp-frame {
    fill: none;
    stroke: var(--ink);
    stroke-width: 4;
    stroke-linecap: butt;
    stroke-linejoin: miter;
  }
  .stamp-text {
    fill: var(--ink);
    font-family: "Poppins", "Century Gothic", sans-serif;
    text-anchor: middle;
  }
  .stamp-name {
    font-size: 44px;
    font-weight: 500;
    letter-spacing: 2.5px;
  }
  .stamp-name .initial {
    font-size: 60px;
  }
  .stamp-web,
  .stamp-mail {
    font-size: 44px;
    font-weight: 600;
    letter-spacing: 1.5px;
  }
</style>
</head>
<body>
  <svg class="stamp-canvas" viewBox="0 0 1200 1000" xmlns="http://www.w3.org/2000/svg">
    <!-- rough stamp border with small ink breaks -->
    <path class="stamp-frame" d="M178 330 L104 329 L103 668 L1096 669 L1096 615" />
    <path class="stamp-frame" d="M1096 588 L1097 330 L225 329" />

    <text class="stamp-text stamp-name" x="600" y="432">
      <tspan class="initial">L</tspan>ucila <tspan class="initial">M</tspan>arbán <tspan class="initial">O</tspan>teiza
    </text>
    <text class="stamp-text stamp-web" x="600" y="522">www.lumaroti.com</text>
    <text class="stamp-text stamp-mail" x="600" y="612">lucilamo47@vextramail.com</text>
  </svg>
</body>
</html>
```